Design a Brochure for Tidal Crate Supplies

We're in need of a product packaging brochure. I've a brochure we currently already have for a different company as inspiration. This brochure should have a similar lay-out. It's a brochure for packaging Materials such as plastic PET bottles, caps, kraft pouches used for food and beverage filling.

1: Front page (I've attached our banner & company logo you can work off, but feel free to spice it up further)
2: Table of content (look at the categories file I've attached to see which categories should be included)
3: Category front page (please make a pitch for this based on 'syrup bottles)
4: Product page (I've included a sketch with what the lay-out should look like as well as an thumbnail of a bottle to use in your pitch)
5: Contact page (www.tidalcratesupplies.example take contact details from there)

Please use your own creativity and surprise me.

UPDATE:

- New categories have been added, please use these ones
- New Bottle thumbnail has bee nadded, please use this one too!

Inspiration for the 'product page' has been added. Our brochure does not incorporate that much information, but this is what a typical page of a product brochure in our industry looks like.

```html
<!DOCTYPE html>
<html lang="en">
<head>
<meta charset="utf-8">
<title>Tidal Crate Supplies – Packaging Brochure</title>
<link rel="stylesheet" href="https://fonts.googleapis.com/css2?family=Arimo:wght@400;700&display=swap">
<style>
  :root {
    --green-deep: #7cbb2e;
    --green-mid: #9fd04c;
    --green-light: #d6f0a2;
    --green-soft: rgba(159, 208, 76, 0);
    --ink-grey: #555a5c;
    --paper: #ffffff;
    --brand-green: #76b82a;
  }
  html, body {
    margin: 0;
    padding: 0;
    overflow: hidden;
    background: var(--paper);
  }
  .cover {
    position: relative;
    width: 848px;
    height: 1200px;
    overflow: hidden;
    background: var(--paper);
    font-family: "Arimo", Arial, sans-serif;
  }
  .cover__waves {
    position: absolute;
    inset: 0;
  }
  .cover__subtitle {
    position: absolute;
    top: 418px;
    left: 0;
    width: 848px;
    margin: 0;
    text-align: center;
    font-size: 24px;
    line-height: 28px;
    font-weight: 400;
    color: var(--ink-grey);
  }
  .brand {
    position: absolute;
    top: 548px;
    left: 0;
    width: 848px;
    display: flex;
    justify-content: center;
    align-items: center;
    gap: 18px;
  }
  .brand__dot {
    flex: none;
    width: 40px;
    height: 40px;
    border-radius: 50%;
    background: var(--brand-green);
  }
  .brand__name {
    margin: 0;
    font-size: 50px;
    line-height: 60px;
    font-weight: 700;
    color: var(--brand-green);
  }
  .scene-factory {
    position: absolute;
    left: 628px;
    top: 872px;
    width: 220px;
    height: 112px;
    border-radius: 60px 0 0 0;
    background:
      linear-gradient(180deg, var(--green-soft) 0%, rgba(159, 208, 76, 0.55) 45%, var(--green-mid) 100%);
  }
  .scene-truck {
    position: absolute;
    left: 424px;
    top: 988px;
    width: 70px;
    height: 38px;
    border-radius: 10px;
    background: radial-gradient(ellipse at 50% 60%, rgba(183, 221, 106, 0.95) 0%, rgba(183, 221, 106, 0.6) 60%, var(--green-soft) 100%);
    transform: rotate(-8deg);
  }
</style>
</head>
<body>
<main class="cover">
  <svg class="cover__waves" width="848" height="1200" viewBox="0 0 848 1200" aria-hidden="true">
    <defs>
      <linearGradient id="topBand" x1="0" y1="0" x2="1" y2="0">
        <stop offset="0" stop-color="#7cbb2e"/>
        <stop offset="0.55" stop-color="#9fd04c"/>
        <stop offset="1" stop-color="#d6f0a2"/>
      </linearGradient>
      <linearGradient id="hill" x1="0" y1="1" x2="1" y2="0">
        <stop offset="0" stop-color="#7cbb2e"/>
        <stop offset="0.6" stop-color="#9fd04c"/>
        <stop offset="1" stop-color="#d6f0a2"/>
      </linearGradient>
    </defs>
    <path class="band-top" d="M0 0 H848 V4 C846 16 830 22 800 24 C560 40 260 40 110 90 C50 110 15 150 0 215 Z" fill="url(#topBand)"/>
    <path class="band-hill" d="M0 1150 C200 1040 480 990 700 980 C770 977 820 978 848 982 V1200 H0 Z" fill="url(#hill)"/>
  </svg>

  <p class="cover__subtitle">Packaging Brochure</p>

  <div class="brand">
    <span class="brand__dot"></span>
    <h1 class="brand__name">Tidal Crate Supplies</h1>
  </div>

  <div class="scene-factory" role="img" aria-label="Green factory buildings with young plants on the hilltop"></div>
  <div class="scene-truck" role="img" aria-label="Small green delivery truck driving over the hill"></div>
</main>
</body>
</html>
```